dsadasdasdasdsa

Industry/Entity Type

Mortgage Broking

Requirements
Must have
• Call-to-action button somewhere on the graphic
Nice to have
• The font of our logo is Montserrat

```html
<!DOCTYPE html>
<html lang="en">
<head>
<meta charset="utf-8">
<title>Mortgage Broker Directory Banner</title>
<link rel="stylesheet" href="https://fonts.googleapis.com/css2?family=Montserrat:wght@500;800;900&display=swap">
<style>
  :root {
    --bg-deep: #0a2e1a;
    --bg-mid: #14532f;
    --bg-glow: #2f9a5a;
    --text-white: #ffffff;
    --text-yellow: #fff200;
    --button-red: #c4301f;
    --button-red-dark: #a3220f;
    --mascot-green: #5fb85a;
    --mascot-brown: #8a5a32;
  }
  html, body {
    margin: 0;
    padding: 0;
    overflow: hidden;
    background: var(--bg-deep);
  }
  .banner {
    position: relative;
    width: 1200px;
    height: 180px;
    overflow: hidden;
    font-family: "Montserrat", Arial, sans-serif;
    background:
      radial-gradient(ellipse 520px 300px at 150px 90px, var(--bg-glow) 0%, var(--bg-mid) 38%, transparent 75%),
      linear-gradient(90deg, var(--bg-mid) 0%, var(--bg-deep) 60%, #0b3320 100%);
  }
  .mascot {
    position: absolute;
    left: 0;
    top: 0;
    width: 225px;
    height: 180px;
    background:
      radial-gradient(ellipse 80px 70px at 120px 60px, var(--mascot-green) 0%, rgba(95,184,90,0.6) 60%, transparent 100%),
      radial-gradient(ellipse 110px 60px at 90px 175px, var(--mascot-brown) 0%, rgba(138,90,50,0.5) 60%, transparent 100%);
  }
  .message {
    position: absolute;
    left: 262px;
    width: 940px;
    top: 22px;
    text-align: center;
  }
  .headline {
    margin: 0;
    color: var(--text-white);
    font-weight: 500;
    font-size: 46px;
    line-height: 1;
    letter-spacing: 0.5px;
    text-transform: uppercase;
  }
  .subline {
    margin: 14px 0 0;
    color: var(--text-yellow);
    font-weight: 900;
    font-size: 34px;
    line-height: 1;
    letter-spacing: -0.2px;
  }
  .cta {
    position: absolute;
    left: 522px;
    top: 133px;
    width: 412px;
    height: 70px;
    border-radius: 35px;
    background: linear-gradient(180deg, var(--button-red) 0%, var(--button-red-dark) 100%);
    color: var(--text-white);
    font-weight: 800;
    font-size: 34px;
    text-align: center;
    line-height: 46px;
    letter-spacing: 0.5px;
    text-decoration: none;
  }
</style>
</head>
<body>
  <div class="banner">
    <div class="mascot" role="img" aria-label="Cartoon turtle mascot smiling and waving"></div>
    <div class="message">
      <h1 class="headline">Need a Mortgage Broker?</h1>
      <p class="subline">Search now on Australia’s largest directory</p>
    </div>
    <a class="cta" href="#">CLICK HERE</a>
  </div>
</body>
</html>
```